" Atendimento individual, observando as necessidades do aluno com especial atenção às lacunas de conhecimento (conteúdos que não foram aprendidos/absorvidos adequadamente e que dificultam a compreensão de novos tópicos). Para tanto, preparamos aulas exclusivas para cada aluno, que é sempre visto como um indivíduo independente que devem ter suas necessidades respeitadas. Dessa forma, trabalhamos para estimular conhecimento, criatividade e autonomia, para vencer dificuldades, enfrentar desafios e formar organização pessoal através de um horário fixo de estudos. "

```html
<!DOCTYPE html>
<html lang="pt-BR">
<head>
<meta charset="UTF-8">
<title>Clara Moreira – Espaço Educacional</title>
<link href="https://fonts.googleapis.com/css2?family=Cinzel:wght@400;600&family=Open+Sans:wght@400;600;700&display=swap" rel="stylesheet">
<style>
  :root {
    --page-bg: #e4e4e4;
    --brand-brown: #8c4a30;
    --brand-brown-light: #a8654a;
    --white: #ffffff;
    --board-green: #41574a;
    --board-green-dark: #2c3d33;
    --desk-wood: #8a5a36;
    --panel-dark: rgba(22, 30, 26, 0.72);
    --line-grey: #b9bdb9;
    --text-light: #f2f2f2;
    --text-muted: #d4d8d4;
  }
  * { margin: 0; padding: 0; box-sizing: border-box; }
  html, body { width: 1200px; height: 1200px; overflow: hidden; }
  body {
    background: var(--page-bg);
    font-family: "Open Sans", Arial, sans-serif;
    position: relative;
  }

  /* ---------- Cover banner ---------- */
  .cover {
    position: absolute;
    left: 91px; top: 211px;
    width: 1003px; height: 382px;
    overflow: hidden;
  }
  .cover-photo {
    position: absolute; inset: 0;
    background:
      linear-gradient(180deg, transparent 0 70%, var(--desk-wood) 70% 100%),
      linear-gradient(90deg, var(--board-green-dark) 0%, var(--board-green) 45%, #4d6656 100%);
  }
  .cover-logo-box {
    position: absolute;
    left: 22px; top: 5px;
    width: 367px; height: 132px;
    background: var(--white);
    display: flex; align-items: center; justify-content: center; gap: 16px;
  }
  .brand-dot {
    width: 34px; height: 34px; border-radius: 50%;
    background: var(--brand-brown);
  }
  .brand-name {
    font-family: "Cinzel", Georgia, serif;
    color: var(--brand-brown);
    font-weight: 400;
    letter-spacing: 0.02em;
    line-height: 1;
  }
  .brand-tag {
    font-family: "Cinzel", Georgia, serif;
    color: var(--brand-brown);
    letter-spacing: 0.28em;
    line-height: 1;
  }
  .cover-logo-box .brand-name { font-size: 30px; }
  .cover-logo-box .brand-tag { font-size: 10px; margin-top: 6px; }

  .connector {
    position: absolute; top: 137px;
    width: 2px; height: 48px;
    background: var(--line-grey);
  }
  .connector::after {
    content: ""; position: absolute;
    left: -6px; bottom: -7px;
    width: 14px; height: 14px; border-radius: 50%;
    background: var(--line-grey);
  }
  .connector.left { left: 64px; }
  .connector.right { left: 346px; }

  .cover-panel {
    position: absolute;
    left: 22px; top: 150px;
    width: 720px; height: 218px;
    background: linear-gradient(90deg, var(--panel-dark) 0%, var(--panel-dark) 50%, rgba(22,30,26,0) 100%);
  }
  .cover-message {
    position: absolute;
    left: 32px; top: 210px;
    width: 680px;
    color: var(--text-light);
    font-size: 14.5px; font-weight: 600;
    line-height: 1.55;
  }

  .contact-row {
    position: absolute;
    left: 32px; top: 296px;
    display: flex; gap: 34px;
  }
  .contact-item {
    display: flex; flex-direction: column; align-items: flex-start; gap: 8px;
    color: var(--text-muted);
    font-size: 9.5px; line-height: 1.35;
  }
  .contact-icon { width: 22px; height: 22px; margin-left: 22px; }
  .contact-item.pin .contact-icon { margin-left: 10px; }

  /* ---------- Logo card ---------- */
  .logo-card {
    position: absolute;
    left: 456px; top: 730px;
    width: 281px; height: 278px;
    background: var(--white);
    display: flex; flex-direction: column; align-items: center; justify-content: center;
  }
  .logo-card .brand-dot { width: 44px; height: 44px; margin-bottom: 26px; }
  .logo-card .brand-name { font-size: 30px; }
  .logo-card .brand-tag { font-size: 9.5px; margin-top: 7px; letter-spacing: 0.3em; }
</style>
</head>
<body>

  <section class="cover">
    <div class="cover-photo" role="img" aria-label="Fotografia de sala de aula: quadro-negro verde com fórmulas, despertador, porta-lápis com lápis coloridos e pilha de livros sobre mesa de madeira"></div>

    <div class="cover-panel"></div>

    <div class="cover-logo-box">
      <span class="brand-dot"></span>
      <div class="brand-lockup">
        <div class="brand-name">Clara Moreira</div>
        <div class="brand-tag">ESPAÇO EDUCACIONAL</div>
      </div>
    </div>

    <span class="connector left"></span>
    <span class="connector right"></span>

    <p class="cover-message">Trabalhamos para estimular o conhecimento, a criatividade<br>e a autonomia para vencer dificuldades, enfrentar desafios.</p>

    <div class="contact-row">
      <div class="contact-item phone">
        <svg class="contact-icon" viewBox="0 0 24 24" aria-hidden="true">
          <circle cx="12" cy="12" r="11" fill="none" stroke="#d4d8d4" stroke-width="1.5"/>
          <path d="M9 7c-1 .6-1.6 1.6-1 3.2.9 2.5 3.3 4.9 5.8 5.8 1.6.6 2.6 0 3.2-1l-1.8-1.6-1.3.8c-1.1-.5-2.6-2-3.1-3.1l.8-1.3z" fill="#d4d8d4"/>
        </svg>
        <span>+55 11 4000-0000<br>+55 11 4000-0001</span>
      </div>
      <div class="contact-item mail">
        <svg class="contact-icon" viewBox="0 0 24 24" aria-hidden="true">
          <circle cx="12" cy="12" r="11" fill="none" stroke="#d4d8d4" stroke-width="1.5"/>
          <rect x="6.5" y="8" width="11" height="8" fill="none" stroke="#d4d8d4" stroke-width="1.4"/>
          <path d="M6.5 8l5.5 4.5L17.5 8" fill="none" stroke="#d4d8d4" stroke-width="1.4"/>
        </svg>
        <span>contato@claramoreira.com.br</span>
      </div>
      <div class="contact-item pin">
        <svg class="contact-icon" viewBox="0 0 24 24" aria-hidden="true">
          <circle cx="12" cy="12" r="11" fill="none" stroke="#d4d8d4" stroke-width="1.5"/>
          <path d="M12 6a4 4 0 0 0-4 4c0 3 4 8 4 8s4-5 4-8a4 4 0 0 0-4-4z" fill="#d4d8d4"/>
          <circle cx="12" cy="10" r="1.5" fill="#2c3d33"/>
        </svg>
        <span>Rua das Acácias, 120<br>Centro | São Paulo | SP | Brasil</span>
      </div>
    </div>
  </section>

  <section class="logo-card">
    <span class="brand-dot"></span>
    <div class="brand-name">Clara Moreira</div>
    <div class="brand-tag">ESPAÇO EDUCACIONAL</div>
  </section>

</body>
</html>
```